National Virtual CPA Firm needs post card design

Virtual CPA firm called "BRELLVO" needs a 5.5” x 8.5” post card designed to market our services to middle market mid-size american businesses. We provide Full Service Payroll (includes the processing of payroll, printing of checks and direct depositing, tax filing, and tax payments), Bookkeeping (Using their native systems, or ours), Contract CFO (with expense reduction analysis), Reporting services for business directors to make informed decisions, Capital Fundraising (Advice on seeking equity to help grow your business), and Taxes (Personal (1040), Partnership (1065), Corporate (1120, 1120S (Including Consolidated Returns)), Trust (1041) and Non-Profit (990)), including all affiliated state returns. One of our major selling points is our variety of experience, and our fast turn around times on projects.
This project specifically, I would like to highlight the bookkeeping services, but still want the tax and payroll services listed on the postcard.
I have uploaded the logo design for BRELLVO and would like a postcard that compliments the logo.
Company contact info is:
Brellvo accounting services Inc
P.O. Box 4638
Alder Bluff, ST 59172
(800) 613-2794
Www.brellvo-example.com
Target Market(s)
Small to medium size businesses
Industry/Entity Type
Accounting
Look and feel

```html
<!DOCTYPE html>
<html lang="en">
<head>
<meta charset="utf-8">
<title>Brellvo Postcard – Front and Back</title>
<link href="https://fonts.googleapis.com/css2?family=Josefin+Sans:wght@300;400;700&family=Open+Sans:wght@400;600;700&display=swap" rel="stylesheet">
<style>
  :root {
    --bg: #e9e9ea;
    --paper: #ffffff;
    --green: #7dbb42;
    --green-dark: #5f9b32;
    --green-deep: #4f8a28;
    --yellow: #f9c512;
    --orange: #f5a81c;
    --ink: #1d1d1d;
    --photo-light: #c4c4c4;
    --photo-dark: #8d8d8d;
  }
  * { box-sizing: border-box; margin: 0; padding: 0; }
  html, body { width: 1200px; height: 800px; overflow: hidden; background: var(--bg); }
  .canvas { position: relative; width: 1200px; height: 800px; }
  .postcard {
    position: absolute; width: 560px; height: 362px;
    background: var(--paper); overflow: hidden;
    box-shadow: 0 6px 18px rgba(0,0,0,.12);
  }
  .postcard--front { left: 26px; top: 219px; }
  .postcard--back { left: 614px; top: 219px; }
  .postcard__art { position: absolute; inset: 0; width: 560px; height: 362px; }
  .brand {
    position: absolute; left: 22px; top: 26px;
    display: flex; align-items: center; gap: 7px;
    font-family: "Josefin Sans", sans-serif; font-weight: 400;
    font-size: 22px; letter-spacing: 1px; color: var(--ink);
  }
  .brand__dot { width: 14px; height: 14px; border-radius: 50%; background: var(--yellow); }
  .headline {
    position: absolute; left: 30px; top: 238px;
    font-family: "Josefin Sans", sans-serif; color: var(--ink);
    font-size: 19px; line-height: 22px; letter-spacing: 4px;
  }
  .headline__strong { font-weight: 700; display: block; }
  .headline__light { font-weight: 300; display: block; }
  .headline__note {
    position: absolute; left: 30px; top: 334px;
    font-family: "Josefin Sans", sans-serif; font-weight: 400;
    font-size: 8px; letter-spacing: 1.5px; line-height: 11px; color: var(--paper);
  }
  .contact { position: absolute; font-family: "Josefin Sans", sans-serif; white-space: nowrap; }
  .contact--front { left: 402px; top: 272px; }
  .contact__label { font-size: 9px; color: var(--green); letter-spacing: 1px; }
  .contact__web { font-size: 11px; color: var(--green-dark); letter-spacing: .6px; font-weight: 400; margin-top: 3px; }
  .contact__phone { font-size: 17px; color: var(--green-dark); letter-spacing: 1.2px; font-weight: 700; margin-top: 3px; }
  .contact--back { left: 352px; top: 252px; color: var(--paper); }
  .contact--back .contact__address { font-size: 8px; letter-spacing: 1px; line-height: 12px; text-transform: uppercase; }
  .contact--back .contact__web, .contact--back .contact__phone { color: var(--paper); }
  .contact--back .contact__web { margin-top: 14px; margin-left: 42px; }
  .contact--back .contact__phone { margin-left: 42px; }
  .services { position: absolute; left: 96px; top: 196px; font-family: "Open Sans", sans-serif; }
  .services__title {
    font-family: "Josefin Sans", sans-serif; font-weight: 700;
    font-size: 24px; letter-spacing: 3px; color: var(--green);
  }
  .services__list { list-style: none; margin-top: 6px; }
  .services__item {
    position: relative; padding-left: 14px; white-space: nowrap;
    font-size: 8px; font-weight: 700; line-height: 15px; color: var(--ink); text-transform: uppercase;
  }
  .services__item::before {
    content: ""; position: absolute; left: 0; top: 4px; width: 5px; height: 5px;
    border-right: 2px solid var(--green); border-bottom: 2px solid var(--green);
    transform: rotate(-45deg);
  }
</style>
</head>
<body>
<main class="canvas">

  <section class="postcard postcard--front" aria-label="Postcard front">
    <svg class="postcard__art" viewBox="0 0 560 362">
      <defs>
        <linearGradient id="photoTone" x1="0" y1="0" x2="1" y2="1">
          <stop offset="0" stop-color="#c4c4c4"/>
          <stop offset="1" stop-color="#8d8d8d"/>
        </linearGradient>
        <linearGradient id="frontGreen" x1="0" y1="0" x2="1" y2="1">
          <stop offset="0" stop-color="#8cc63f"/>
          <stop offset="1" stop-color="#5f9b32"/>
        </linearGradient>
      </defs>
      <path role="img" aria-label="Photo of a desk from above with a laptop, coffee cup, calculator and hands typing"
            d="M255 0 H560 V110 C540 185 470 212 400 214 H255 Z" fill="url(#photoTone)"/>
      <path d="M80 305 C100 170 220 96 340 110 C420 120 455 168 505 188 C430 214 300 196 200 206 C140 212 100 245 80 305 Z"
            fill="var(--yellow)" opacity="0.9"/>
      <path d="M0 362 V238 C60 215 150 205 260 208 C380 212 470 200 530 120 L548 118 C505 205 430 228 335 232 L378 362 Z"
            fill="url(#frontGreen)"/>
      <path d="M548 70 C540 160 480 215 400 222" fill="none" stroke="var(--green)" stroke-width="4"/>
      <circle cx="458" cy="150" r="44" fill="var(--paper)"/>
      <circle cx="458" cy="150" r="38" fill="var(--green)"/>
      <circle cx="378" cy="310" r="18" fill="var(--green)"/>
      <path d="M371 302 c-3 3 -2 9 4 15 s12 7 15 4 l2 -3 -5 -4 -3 3 c-3 -1 -7 -5 -8 -8 l3 -3 -4 -5 Z" fill="var(--paper)"/>
    </svg>
    <div class="brand"><span class="brand__dot"></span>BRELLVO</div>
    <h2 class="headline">
      <span class="headline__strong">VARIETY OF</span>
      <span class="headline__strong">EXPERIENCE,</span>
      <span class="headline__strong">FAST TURN</span>
      <span class="headline__light">AROUND</span>
    </h2>
    <p class="headline__note">ONE OF OUR MAJOR<br>SELLING POINTS IS OUR</p>
    <div class="contact contact--front">
      <p class="contact__label">Contact Us</p>
      <p class="contact__web">www.brellvo-example.com</p>
      <p class="contact__phone">(800) 613-2794</p>
    </div>
  </section>

  <section class="postcard postcard--back" aria-label="Postcard back">
    <svg class="postcard__art" viewBox="0 0 560 362" aria-hidden="true">
      <defs>
        <linearGradient id="swoosh" x1="0" y1="0" x2="1" y2="0">
          <stop offset="0" stop-color="#f9c512"/>
          <stop offset="1" stop-color="#f5a81c"/>
        </linearGradient>
        <linearGradient id="backGreen" x1="0" y1="0" x2="1" y2="1">
          <stop offset="0" stop-color="#7dbb42"/>
          <stop offset="1" stop-color="#5f9b32"/>
        </linearGradient>
      </defs>
      <path d="M115 235 C140 160 240 128 330 128 C410 128 460 108 510 62 C485 130 430 162 360 170 C270 180 170 178 115 235 Z"
            fill="url(#swoosh)"/>
      <path d="M336 362 V232 C430 232 512 190 540 50 L560 45 V362 Z" fill="url(#backGreen)"/>
      <path d="M336 226 C430 226 504 185 532 40" fill="none" stroke="var(--paper)" stroke-width="6"/>
      <circle cx="370" cy="318" r="18" fill="var(--green-deep)"/>
      <path d="M363 310 c-3 3 -2 9 4 15 s12 7 15 4 l2 -3 -5 -4 -3 3 c-3 -1 -7 -5 -8 -8 l3 -3 -4 -5 Z" fill="var(--paper)"/>
    </svg>
    <div class="brand"><span class="brand__dot"></span>BRELLVO</div>
    <div class="services">
      <h2 class="services__title">SERVICES</h2>
      <ul class="services__list">
        <li class="services__item">Full service payroll</li>
        <li class="services__item">Bookkeeping</li>
        <li class="services__item">Contract CFO</li>
        <li class="services__item">Reporting services for business</li>
        <li class="services__item">Directors</li>
        <li class="services__item">And taxes</li>
        <li class="services__item">Corporate</li>
        <li class="services__item">Including all affiliated state returns</li>
      </ul>
    </div>
    <div class="contact contact--back">
      <p class="contact__address">Brellvo accounting services Inc<br>P.O. Box 4638<br>Alder Bluff, ST 59172</p>
      <p class="contact__web">www.brellvo-example.com</p>
      <p class="contact__phone">(800) 613-2794</p>
    </div>
  </section>

</main>
</body>
</html>
```